Book cover design for an inspirational book on "Velvendary" Living

Velvendary Dwelling is a phase I have coined to describe inspirational life principles that emerge by following your passion in life. My passion is shabby chic furniture and décor. I run an on-line business called Dearly Kept Goods - see my web site www.dearlykeptgoods.com.au and the links to my Chatterbook page (daily inspiration) and my ClipStream channel - Velvendary TV to get a fuller sense of my passion.

The Book is loosely modelled on the "Warm Bread for the Weary" formula with the exception all of the stories are my own. I tell stories about pieces of furniture that I have created and demonstrate essential life lessons and principles though those creations. Examples of the life lessons (to help illustrate) include the importance of living in the now, overcoming obstacles in life, following your passion and love. The vehicle to carry these messages is Shabby Chic - my passion.

The title of the book is Velvendary Dwelling - Worn Tales of Warmth, Drive and Uplift. The author is my partner - Mira Tolk. I was intending this to be an e-book in the first instance with an option to go to print.
Updates

please see new addition of pictures and writing preference in script ,                                    

instead of stories of passion and love, to replace with   Follow your passion and create from your heart , (symbol of heart) at the side of end ...maybe ..  

Finding and following  your passion

Target Market(s)

Women across a fairly broad spectrum of 20's to mid 60's.

People interested in "new age" in the sense of finding and following your life passion.

Positive energy and traditional principles of happy home, family and passion for living and life.

Industry/Entity Type

Business

Font styles to use
Script

Colors
eea4c8

Requirements
Must have
• The book is inspirational and heart warming so the design should carry a positive energy that catches the eye and invites the reader to open the book to find out more.
Nice to have
• A shabby chic feel and style. My favourite colour is pink and I adore roses but this is not mandatory. The current visitor profile to my Chatterbook and ClipStream sites is 85% female generally between the early 20's to the mid 60's in age.

I am more interested in classy and positive than "girly". I am aiming the book at both genders but realise the appeal will be greatest to women.
Should not have
• I am looking for unique so want to be different than say Odette Pruvin who is one of the leaders in the world of shabby chic. The book is from me, so whilst I have provided my logo, I don't think it needs to feature in the design necessarily.

```html
<!DOCTYPE html>
<html lang="en">
<head>
<meta charset="utf-8">
<title>Velvendary Dwelling – Book Cover</title>
<link href="https://fonts.googleapis.com/css2?family=Marcellus&family=Open+Sans:wght@400;600&display=swap" rel="stylesheet">
<style>
  :root {
    --paper: #ffffff;
    --wash-blue: #d6ecf0;
    --wash-green: #e3f1e6;
    --title-pink: #e2458f;
    --subtitle-gold: #a88a2c;
    --hill-lilac: #cfc3dc;
    --hill-shade: #b9aacb;
    --art-pink: #f6c8dc;
    --art-cream: #f3eedb;
    --author-ink: #4a3f55;
  }
  * { margin: 0; padding: 0; box-sizing: border-box; }
  html, body {
    width: 982px;
    height: 1200px;
    overflow: hidden;
    background: var(--paper);
  }
  .cover {
    position: relative;
    width: 982px;
    height: 1200px;
    background: var(--paper);
    overflow: hidden;
  }
  .cover__wash {
    position: absolute;
    inset: 0 0 auto 0;
    height: 620px;
    background:
      radial-gradient(ellipse 70% 55% at 50% 8%, var(--wash-blue) 0%, rgba(214,236,240,0) 70%),
      radial-gradient(ellipse 45% 35% at 78% 52%, var(--wash-green) 0%, rgba(227,241,230,0) 70%),
      radial-gradient(ellipse 45% 35% at 20% 58%, var(--wash-green) 0%, rgba(227,241,230,0) 70%);
  }
  .cover__title {
    position: absolute;
    top: 95px;
    left: 0;
    right: 0;
    text-align: center;
    font-family: "Marcellus", serif;
    color: var(--title-pink);
    font-weight: 400;
    line-height: 1;
  }
  .cover__title-top {
    display: block;
    font-size: 104px;
    letter-spacing: 1px;
  }
  .cover__title-bottom {
    display: block;
    margin-top: 22px;
    font-size: 150px;
  }
  .cover__subtitle {
    position: absolute;
    top: 440px;
    left: 0;
    right: 0;
    text-align: center;
    font-family: "Open Sans", sans-serif;
    font-size: 38px;
    line-height: 1.3;
    color: var(--subtitle-gold);
  }
  .cover__art {
    position: absolute;
    left: 0;
    right: 0;
    top: 640px;
    height: 440px;
    background:
      radial-gradient(ellipse 40% 50% at 50% 55%, var(--art-pink) 0%, rgba(246,200,220,0) 75%),
      linear-gradient(180deg, rgba(243,238,219,0) 0%, var(--art-cream) 100%);
  }
  .cover__hill {
    position: absolute;
    left: 0;
    bottom: 0;
    width: 982px;
    height: 220px;
  }
  .cover__author {
    position: absolute;
    left: 0;
    right: 0;
    bottom: 62px;
    text-align: center;
    font-family: "Open Sans", sans-serif;
    font-size: 40px;
    letter-spacing: 14px;
    color: var(--author-ink);
  }
</style>
</head>
<body>
  <main class="cover">
    <div class="cover__wash"></div>

    <h1 class="cover__title">
      <span class="cover__title-top">Velvendary</span>
      <span class="cover__title-bottom">Dwelling</span>
    </h1>

    <p class="cover__subtitle">Worn Tales of Warmth,<br>Drive and Uplift</p>

    <div class="cover__art" role="img" aria-label="Illustration of two small birds sharing hearts among pastel flower pots with heart-shaped sprouts"></div>

    <svg class="cover__hill" viewBox="0 0 982 220" aria-hidden="true">
      <path d="M0 70 C 250 20, 700 10, 982 60 L 982 220 L 0 220 Z" fill="var(--hill-lilac)"/>
      <path d="M0 150 C 300 120, 700 125, 982 155 L 982 220 L 0 220 Z" fill="var(--hill-shade)" opacity="0.45"/>
    </svg>

    <p class="cover__author">Mira Tolk</p>
  </main>
</body>
</html>
```